Argan Oil Shampoo/Conditioner Label

We are looking for 2 label designs. One for a shampoo bottle, and one for a conditioner bottle. The designs will be similar, however on the conditioner bottle, on the bottom of the label we would like a colored line across acting as a visual indicator to distinguish the two bottles.
Update - Brand name is being finalized but instead of meridian use "Velour - Concept use a raindrop in place of the apostrophe. And smaller font for “Velour” directly under “Belu’s”
As for the label, we are looking for a background design for the label as well as some concepts for the main product information and we will need to add the ingredients and instructions later.
Concepts for the Product label, the shampoo and conditioner is going to consist of Argan Oil, so having a black silhouette of an argan tree.
We don’t want something too extravagant or gaudy. Something simple but will make the product look high class. This will be a premium product and we want the label to portray that.
Update- The label dimensions are estimated to be 7.75" wrapped around the bottle. The height of the label will be estimated at 5" from top to bottom.
Please use your artistic minds, we are open to other ideas and concepts as well with keeping to the above mentioned restrictions of not being too gaudy and extravagant.
We are seeking some revisions from a designer and are wanting to give him some more time.

```html
<!DOCTYPE html>
<html lang="en">
<head>
<meta charset="utf-8">
<title>Belu’s Velour – Shampoo &amp; Conditioner Labels</title>
<link rel="stylesheet" href="https://fonts.googleapis.com/css2?family=Lato:wght@400;700&family=Comfortaa:wght@400&display=swap">
<style>
  :root {
    --page-bg: #eff0f2;
    --label-white: #ffffff;
    --charcoal: #2a2a2a;
    --wave-dark: #3a3a3c;
    --tree-tone: #2f2f31;
    --accent-orange: #f0562a;
    --ink: #ffffff;
    --logo-ink: #242223;
  }
  * { box-sizing: border-box; margin: 0; padding: 0; }
  html, body {
    width: 1200px; height: 1138px; overflow: hidden;
    background: var(--page-bg);
    font-family: "Lato", sans-serif;
  }
  .label {
    position: absolute; left: 98px;
    width: 1005px; height: 480px;
    background: var(--label-white);
    overflow: hidden;
  }
  .label--shampoo { top: 76px; }
  .label--conditioner { top: 594px; }

  .label__art { position: absolute; left: 0; top: 0; width: 512px; height: 480px; }

  .brand {
    position: absolute; left: 215px; top: 32px; width: 250px;
    color: var(--logo-ink); font-family: "Lato", sans-serif; font-weight: 400;
    text-align: right;
  }
  .brand__name { display: block; font-size: 78px; line-height: 1; letter-spacing: 1px; }
  .brand__sub { display: block; font-size: 54px; line-height: 1.1; letter-spacing: 2px; }
  .brand__dot {
    position: absolute; right: -8px; top: 4px;
    width: 14px; height: 14px; border-radius: 50%;
    background: var(--accent-orange);
  }

  .product-name {
    position: absolute; left: 106px; bottom: 36px;
    font-family: "Comfortaa", sans-serif; font-size: 40px;
    color: var(--accent-orange); letter-spacing: 1px;
  }

  .info-panel {
    position: absolute; left: 511px; top: 8px;
    width: 485px; height: 464px;
    background: var(--charcoal); color: var(--ink);
  }
  .info-section { position: absolute; left: 0; width: 100%; text-align: center; }
  .info-section h2 { font-size: 21px; font-weight: 700; line-height: 1; margin-bottom: 9px; }
  .info-section p { font-size: 13.4px; line-height: 17.2px; padding: 0 20px; }
  .info-section--philosophy { top: 24px; }
  .info-section--product { top: 151px; }
  .info-section--stylist { top: 259px; }
  .divider {
    position: absolute; left: 8px; right: 8px; height: 2px; background: var(--ink);
  }
  .divider--one { top: 137px; }
  .divider--two { top: 245px; }

  .company { position: absolute; left: 20px; top: 378px; }
  .company__name { font-size: 16.5px; font-weight: 700; margin-bottom: 4px; }
  .company__address { font-size: 12.4px; line-height: 16px; }

  .barcode-box {
    position: absolute; left: 277px; top: 373px; width: 188px; height: 67px;
    background: var(--label-white); color: var(--charcoal);
    display: flex; align-items: center; justify-content: center;
    font-size: 20px;
  }
</style>
</head>
<body>

<section class="label label--shampoo">
  <svg class="label__art" viewBox="0 0 640 600" preserveAspectRatio="none" aria-hidden="false">
    <path fill="var(--wave-dark)" d="M0,12 C12,190 140,250 320,312 C460,360 545,455 578,600 L0,600 Z"/>
    <g role="img" aria-label="Dark silhouette of an argan tree">
      <path fill="var(--tree-tone)" d="M0,280 C80,250 190,300 250,360 C290,420 230,470 150,470 C110,520 90,570 85,600 L0,600 Z"/>
    </g>
    <path fill="var(--accent-orange)" d="M0,0 L4,0 C22,170 150,232 335,292 C485,342 570,440 596,600 L580,600 C548,455 462,360 322,312 C140,250 12,190 0,12 Z"/>
    <path fill="var(--accent-orange)" d="M30,62 C44,172 158,228 322,278 C455,320 545,385 598,460 C530,400 445,350 310,305 C142,250 32,190 30,62 Z"/>
  </svg>
  <div class="brand"><span class="brand__dot"></span><span class="brand__name">Belu’s</span><span class="brand__sub">Velour</span></div>
  <div class="product-name">shampoo</div>
  <div class="info-panel">
    <div class="info-section info-section--philosophy">
      <h2>OUR PHILOSOPHY</h2>
      <p>Lorem ipsum dolor sit amet, consectetuer adipiscing elit, sed diam nonummy nibh euismod tincidunt ut laoreet dolore magna aliquam erat volutpat. Ut wisi enim ad minim veniam, quis nostrud exerci tation ullamcorper suscipit lobortis nisl ut aliquip ex ea commodo consequat.</p>
    </div>
    <div class="divider divider--one"></div>
    <div class="info-section info-section--product">
      <h2>THIS PRODUCT</h2>
      <p>Lorem ipsum dolor sit amet, consectetuer adipiscing elit, sed diam nonummy nibh euismod tincidunt ut laoreet dolore magna aliquam erat volutpat. Ut wisi enim ad minim veniam.</p>
    </div>
    <div class="divider divider--two"></div>
    <div class="info-section info-section--stylist">
      <h2>OUR LEAD STYLIST SUGGESTS</h2>
      <p>Lorem ipsum dolor sit amet, consectetuer adipiscing elit, sed diam nonummy nibh euismod tincidunt ut laoreet dolore magna aliquam erat volutpat. Ut wisi enim ad minim veniam, quis nostrud exerci tation ullamcorper suscipit lobortis nisl ut aliquip ex ea commodo consequat.</p>
    </div>
    <div class="company">
      <div class="company__name">Belu’s Velour private limited</div>
      <div class="company__address">Address here please, address here please<br>address here: Ph:000 0000 0000</div>
    </div>
    <div class="barcode-box">Bar code</div>
  </div>
</section>

<section class="label label--conditioner">
  <svg class="label__art" viewBox="0 0 640 600" preserveAspectRatio="none" aria-hidden="false">
    <path fill="var(--wave-dark)" d="M0,12 C12,190 140,250 320,312 C460,360 545,455 578,600 L0,600 Z"/>
    <g role="img" aria-label="Dark silhouette of an argan tree">
      <path fill="var(--tree-tone)" d="M0,280 C80,250 190,300 250,360 C290,420 230,470 150,470 C110,520 90,570 85,600 L0,600 Z"/>
    </g>
    <path fill="var(--accent-orange)" d="M0,0 L4,0 C22,170 150,232 335,292 C485,342 570,440 596,600 L580,600 C548,455 462,360 322,312 C140,250 12,190 0,12 Z"/>
    <path fill="var(--accent-orange)" d="M30,62 C44,172 158,228 322,278 C455,320 545,385 598,460 C530,400 445,350 310,305 C142,250 32,190 30,62 Z"/>
  </svg>
  <div class="brand"><span class="brand__dot"></span><span class="brand__name">Belu’s</span><span class="brand__sub">Velour</span></div>
  <div class="product-name">conditioner</div>
  <div class="info-panel">
    <div class="info-section info-section--philosophy">
      <h2>OUR PHILOSOPHY</h2>
      <p>Lorem ipsum dolor sit amet, consectetuer adipiscing elit, sed diam nonummy nibh euismod tincidunt ut laoreet dolore magna aliquam erat volutpat. Ut wisi enim ad minim veniam, quis nostrud exerci tation ullamcorper suscipit lobortis nisl ut aliquip ex ea commodo consequat.</p>
    </div>
    <div class="divider divider--one"></div>
    <div class="info-section info-section--product">
      <h2>THIS PRODUCT</h2>
      <p>Lorem ipsum dolor sit amet, consectetuer adipiscing elit, sed diam nonummy nibh euismod tincidunt ut laoreet dolore magna aliquam erat volutpat. Ut wisi enim ad minim veniam.</p>
    </div>
    <div class="divider divider--two"></div>
    <div class="info-section info-section--stylist">
      <h2>OUR LEAD STYLIST SUGGESTS</h2>
      <p>Lorem ipsum dolor sit amet, consectetuer adipiscing elit, sed diam nonummy nibh euismod tincidunt ut laoreet dolore magna aliquam erat volutpat. Ut wisi enim ad minim veniam, quis nostrud exerci tation ullamcorper suscipit lobortis nisl ut aliquip ex ea commodo consequat.</p>
    </div>
    <div class="company">
      <div class="company__name">Belu’s Velour private limited</div>
      <div class="company__address">Address here please, address here please<br>address here: Ph:000 0000 0000</div>
    </div>
    <div class="barcode-box">Bar code</div>
  </div>
</section>

</body>
</html>
```